Korvell Plant Services

We are a heavy diesel mechanical business with additional air con certificates, remapping engine rebuilt

Contact Information for Business Card

Company Name, Director Name, Managing Director, Contact details, email and website

Font styles to use
Serif
Script

```html
<!DOCTYPE html>
<html lang="en">
<head>
<meta charset="utf-8">
<title>Korvell Plant Services – Business Card</title>
<link href="https://fonts.googleapis.com/css2?family=Open+Sans:wght@400;600;700&display=swap" rel="stylesheet">
<style>
  :root {
    --navy: #24226a;
    --ink: #111111;
    --paper: #ffffff;
    --muted: #2a2a2a;
    --backdrop: #3b3b3b;
  }
  * { box-sizing: border-box; margin: 0; padding: 0; }
  html, body { width: 1200px; height: 780px; overflow: hidden; }
  body {
    background: var(--backdrop);
    font-family: "Open Sans", Arial, sans-serif;
    position: relative;
  }
  .card {
    position: absolute;
    top: 240px;
    width: 520px;
    height: 300px;
    background: var(--paper);
    border-radius: 22px;
    overflow: hidden;
  }
  .card--front { left: 50px; }
  .card--back { left: 630px; }

  .front-band { position: absolute; inset: 0; }

  .brand {
    font-family: "Open Sans", Arial, sans-serif;
    font-weight: 700;
    color: var(--navy);
    display: flex;
    align-items: center;
    gap: 10px;
    line-height: 1.05;
  }
  .brand__dot {
    flex: none;
    border-radius: 50%;
    background: var(--navy);
  }
  .brand--small {
    position: absolute;
    left: 232px;
    top: 38px;
    font-size: 26px;
    width: 240px;
  }
  .brand--small .brand__dot { width: 18px; height: 18px; }

  .holder {
    position: absolute;
    left: 38px;
    top: 70px;
  }
  .holder__name {
    font-weight: 700;
    font-size: 19px;
    color: var(--navy);
    letter-spacing: 0.3px;
  }
  .holder__role {
    font-size: 13px;
    color: var(--muted);
    margin-top: 2px;
  }
  .divider {
    position: absolute;
    left: 212px;
    top: 128px;
    width: 1.5px;
    height: 64px;
    background: var(--navy);
  }
  .contacts {
    position: absolute;
    left: 230px;
    top: 136px;
    list-style: none;
    font-size: 14px;
    color: var(--ink);
  }
  .contacts li {
    display: flex;
    align-items: center;
    gap: 7px;
    height: 19px;
  }
  .contacts svg { width: 11px; height: 11px; flex: none; }
  .address {
    position: absolute;
    left: 40px;
    top: 264px;
    font-size: 14px;
    color: var(--paper);
  }

  .brand--large {
    position: absolute;
    left: 0; right: 0; top: 0; bottom: 0;
    justify-content: center;
    font-size: 40px;
    text-align: center;
  }
  .brand--large .brand__dot { width: 26px; height: 26px; }
</style>
</head>
<body>

  <section class="card card--front" aria-label="Business card front">
    <svg class="front-band" viewBox="0 0 520 300" aria-hidden="true">
      <path d="M0,166 Q170,250 520,228" fill="none" stroke="var(--ink)" stroke-width="3"/>
      <path d="M0,176 Q170,260 520,238 L520,300 L0,300 Z" fill="var(--navy)"/>
    </svg>

    <div class="brand brand--small">
      <span class="brand__dot"></span>
      <span>Korvell Plant Services</span>
    </div>

    <div class="holder">
      <p class="holder__name">TOMAS REYNE</p>
      <p class="holder__role">Managing Director</p>
    </div>

    <span class="divider"></span>

    <ul class="contacts">
      <li>
        <svg viewBox="0 0 12 12" aria-hidden="true"><path d="M3 1 L5 3 L4 4.5 Q5 7 7.5 8 L9 7 L11 9 L9.5 11 Q2 10 1 2.5 Z" fill="var(--navy)"/></svg>
        <span>123 456 789</span>
      </li>
      <li>
        <svg viewBox="0 0 12 12" aria-hidden="true"><rect x="1" y="2.5" width="10" height="7" fill="var(--navy)"/><path d="M1 2.5 L6 6.5 L11 2.5" fill="none" stroke="#fff" stroke-width="1"/></svg>
        <span>info@korvellplant.com</span>
      </li>
      <li>
        <svg viewBox="0 0 12 12" aria-hidden="true"><circle cx="6" cy="6" r="5" fill="var(--navy)"/><path d="M1 6 H11 M6 1 Q3 6 6 11 M6 1 Q9 6 6 11" fill="none" stroke="#fff" stroke-width="0.8"/></svg>
        <span>www.korvellplant.com</span>
      </li>
    </ul>

    <p class="address">Your address, City State, Zip 1234</p>
  </section>

  <section class="card card--back" aria-label="Business card back">
    <div class="brand brand--large">
      <span class="brand__dot"></span>
      <span>Korvell Plant Services</span>
    </div>
  </section>

</body>
</html>
```